Legal Service Estimated Retainer and Average Case Value

We need an 11x14 flyer that contains the standard retainers and average cost be case, both provided in documents, for each case type we handle. We need the information displayed, preferably in a way that makes the information readable but less troubling to a client shocked at price of litigation. We need one sheet with the retainers and average case value merged into one table.

Target Market(s)

Potential Clients

Font styles to use
Serif
Sans Serif

```html
<!DOCTYPE html>
<html lang="en">
<head>
<meta charset="utf-8">
<title>Fee Per Case Type — The Law Office of Daniel M Whitfield</title>
<link rel="stylesheet" href="https://fonts.googleapis.com/css2?family=Cinzel:wght@600;700&family=Bitter:wght@400&family=Montserrat:wght@500&display=swap">
<style>
  :root {
    --navy: #12163f;
    --ink: #4d4d57;
    --row: #f1f1f4;
    --paper: #ffffff;
    --bg-top: #e9ecf2;
    --bg-bottom: #f7f8fb;
    --photo-a: #3c5a3a;
    --photo-b: #c9a27e;
    --photo-c: #7e5a4a;
  }
  * { margin: 0; padding: 0; box-sizing: border-box; }
  html, body { width: 943px; height: 1200px; overflow: hidden; }
  body {
    position: relative;
    background: linear-gradient(160deg, var(--bg-top) 0%, #f4f5f8 45%, var(--bg-bottom) 100%);
    font-family: "Bitter", Georgia, serif;
    color: var(--ink);
  }
  .backdrop {
    position: absolute; inset: 27px 0 30px 0;
    background: linear-gradient(90deg, rgba(200,205,215,.35) 0%, rgba(255,255,255,.6) 30%, rgba(210,214,224,.3) 55%, rgba(255,255,255,.5) 100%);
  }
  .band-top { position: absolute; left: 0; top: 0; width: 943px; height: 27px; background: var(--navy); }
  .band-bottom { position: absolute; left: 0; bottom: 0; width: 943px; height: 30px; background: var(--navy); }

  .photo { position: absolute; left: 553px; top: 13px; width: 372px; height: 458px; }

  .firm {
    position: absolute; left: 81px; top: 88px;
    font-family: "Cinzel", Georgia, serif; font-weight: 600; color: var(--navy);
    line-height: 1;
  }
  .firm-prefix { display: block; font-size: 12.5px; letter-spacing: .5px; margin-bottom: 3px; }
  .firm-name { display: block; font-size: 27px; letter-spacing: .3px; }

  .title {
    position: absolute; left: 80px; top: 190px;
    font-family: "Cinzel", Georgia, serif; font-weight: 700; color: var(--navy);
    font-size: 55px; line-height: 48px; letter-spacing: .5px;
  }

  .intro {
    position: absolute; left: 79px; top: 313px; width: 475px;
    font-size: 16.6px; line-height: 22.9px; color: var(--ink);
  }

  .fees {
    position: absolute; left: 72px; top: 485px; width: 798px; height: 631px;
    background: var(--paper); border: 2px solid var(--navy);
  }
  .fees-head { position: absolute; top: 0; left: 0; width: 100%; height: 26px; }
  .col-head {
    position: absolute; top: 0; height: 26px;
    background: var(--navy); color: #fff;
    font-family: "Montserrat", Arial, sans-serif; font-weight: 500; font-size: 17px;
    display: flex; align-items: center; justify-content: center;
  }
  .col-head.retainer { left: 467px; width: 113px; }
  .col-head.average { left: 592px; width: 190px; }

  .fees-body { position: absolute; left: 0; top: 38px; width: 100%; }
  .fee-row {
    height: 44.6px; display: flex; align-items: center;
    font-size: 17px; color: var(--ink);
  }
  .fee-row:nth-child(odd) {
    background: linear-gradient(transparent 0, transparent 5px, var(--row) 5px, var(--row) 39px, transparent 39px);
  }
  .case { width: 467px; padding-left: 32px; white-space: nowrap; }
  .retainer-amt { width: 113px; text-align: center; }
  .average-amt { width: 190px; margin-left: 12px; text-align: center; }
</style>
</head>
<body>
  <div class="backdrop" role="img" aria-label="Soft, faded photograph of white classical columns"></div>
  <div class="band-top"></div>
  <div class="band-bottom"></div>

  <svg class="photo" viewBox="0 0 372 458" role="img" aria-label="Photograph of a smiling couple embracing outdoors in front of greenery">
    <defs>
      <linearGradient id="photoTone" x1="0" y1="0" x2="1" y2="1">
        <stop offset="0" stop-color="var(--photo-a)"/>
        <stop offset=".55" stop-color="var(--photo-b)"/>
        <stop offset="1" stop-color="var(--photo-c)"/>
      </linearGradient>
    </defs>
    <path d="M0 0 H372 V235 C372 335 300 420 186 458 C72 420 0 335 0 235 Z" fill="url(#photoTone)"/>
  </svg>

  <div class="firm">
    <span class="firm-prefix">The Law Office of</span>
    <span class="firm-name">Daniel M Whitfield</span>
  </div>

  <h1 class="title">Fee Per<br>Case Type</h1>

  <p class="intro">In order for our clients to set expectations for legal fees, we provide the national average range of fees per case type. These are only to provide you with an understanding of what other cases have cost clients in similar cases. Please note these are not estimates nor guarantees of your own legal costs.</p>

  <section class="fees">
    <div class="fees-head">
      <div class="col-head retainer">Retainer</div>
      <div class="col-head average">Average Fee</div>
    </div>
    <div class="fees-body">
      <div class="fee-row"><span class="case">Divorce (3301 C)</span><span class="retainer-amt">$2,000</span><span class="average-amt">$1,500 - $3,000</span></div>
      <div class="fee-row"><span class="case">Divorce (3301 D)</span><span class="retainer-amt">$2,500</span><span class="average-amt">$2,000 - $3,000</span></div>
      <div class="fee-row"><span class="case">Custody Initial Order</span><span class="retainer-amt">$3,000</span><span class="average-amt">$4,000 - $7,000</span></div>
      <div class="fee-row"><span class="case">Custody Contempt/Modification</span><span class="retainer-amt">$3,500</span><span class="average-amt">$5,000 - $8,000</span></div>
      <div class="fee-row"><span class="case">Custody &amp; Support</span><span class="retainer-amt">$3,000</span><span class="average-amt">$5,000 - $8,000</span></div>
      <div class="fee-row"><span class="case">Divorce &amp; Support</span><span class="retainer-amt">$3,000</span><span class="average-amt">$2,000 - $4,000</span></div>
      <div class="fee-row"><span class="case">Divorce &amp; Custody</span><span class="retainer-amt">$3,500</span><span class="average-amt">$5,000 - $8,000</span></div>
      <div class="fee-row"><span class="case">Divorce &amp; Equitable Distribution</span><span class="retainer-amt">$3,500</span><span class="average-amt">$6,000 - $10,000</span></div>
      <div class="fee-row"><span class="case">Divorce, Custody &amp; Support</span><span class="retainer-amt">$3,500</span><span class="average-amt">$8,000 - $12,000</span></div>
      <div class="fee-row"><span class="case">Divorce, Equitable Distribution &amp; Custody</span><span class="retainer-amt">$5,000</span><span class="average-amt">$10,000 - $15,000</span></div>
      <div class="fee-row"><span class="case">Divorce, Equitable Distribution &amp; Support</span><span class="retainer-amt">$3,500</span><span class="average-amt">$8,000 - $12,000</span></div>
      <div class="fee-row"><span class="case">Divorce, Equitable Distribution, Custody &amp; Support</span><span class="retainer-amt">$3,500</span><span class="average-amt">$12,000 - $15,000</span></div>
      <div class="fee-row"><span class="case">Protection from Abuse</span><span class="retainer-amt">$2,000</span><span class="average-amt">$1,500 - $3,000</span></div>
    </div>
  </section>
</body>
</html>
```